Velvor IT Services Business Card

Velvor IT Services are a Perth based IT Services company. We would like to incorporate our company logo (attached) and stick with the blue that is in that design. I would like a clean look design that isn't too busy, yet creates a lasting image that is instantly recognisable in the recipients mind.

Target Market(s)

The target audience is small/medium business owners.

Industry/Entity Type

Business

Font styles to use
Serif
Sans Serif

Colors

Designer to choose colors to be used in the design.

Requirements
Must have
• The design should include:
Business name: Velvor IT Services
Directors Name: Marcus Dredge
Phone Number: 0483 906 452
Email: support@velvorit.com.au
Website: www.velvorit.com.au

```html
<!DOCTYPE html>
<html lang="en">
<head>
<meta charset="utf-8">
<title>Velvor IT Services Business Card</title>
<link rel="stylesheet" href="https://fonts.googleapis.com/css2?family=Lato:wght@400;700;900&display=swap">
<style>
  :root {
    --sky: #33b5ea;
    --sky-deep: #1f9fd8;
    --navy: #14285c;
    --ink: #0b0b0d;
    --paper: #ffffff;
    --paper-shade: #e9ecef;
    --mist: #d9dde2;
    --stage: #2a2b2e;
  }
  * { box-sizing: border-box; margin: 0; padding: 0; }
  html, body { width: 1200px; height: 900px; overflow: hidden; }
  body {
    background: var(--stage);
    font-family: "Lato", Arial, sans-serif;
    position: relative;
  }
  .card {
    position: absolute;
    left: 250px;
    width: 700px;
    height: 400px;
    overflow: hidden;
    box-shadow: 0 12px 30px rgba(0,0,0,.5);
  }
  /* Back */
  .card-back { top: 30px; background: var(--sky); }
  .card-back .headline {
    position: absolute; left: 0; right: 0; top: 0; height: 330px;
    display: flex; align-items: center; justify-content: center;
    text-align: center;
    color: var(--paper);
    font-weight: 700; font-size: 42px; line-height: 1.35;
    letter-spacing: .5px;
    text-shadow: 0 0 10px rgba(255,255,255,.45);
  }
  .card-back .footer-strip {
    position: absolute; left: 0; right: 0; bottom: 0; height: 70px;
    background: var(--ink);
    color: var(--paper);
    display: flex; align-items: center; justify-content: center;
    font-weight: 900; font-size: 19px; letter-spacing: .3px;
  }
  /* Front */
  .card-front { top: 470px; background: linear-gradient(180deg, var(--paper) 0%, var(--paper-shade) 100%); }
  .name-tag {
    position: absolute; left: -20px; top: 100px;
    background: var(--sky);
    color: var(--paper);
    font-weight: 900; font-size: 26px;
    padding: 10px 34px 10px 48px;
    border-radius: 0 26px 26px 0;
  }
  .brand {
    position: absolute; right: 60px; top: 62px;
    display: flex; align-items: center; gap: 14px;
  }
  .brand-mark { width: 46px; height: 46px; background: var(--sky-deep); }
  .brand-name {
    color: var(--navy);
    font-weight: 900; font-size: 34px; letter-spacing: 1px;
  }
  .website {
    position: absolute; right: 60px; top: 172px;
    display: flex; align-items: center; gap: 8px;
    color: var(--navy); font-weight: 700; font-size: 17px;
  }
  .info-band {
    position: absolute; left: 0; right: 0; top: 205px; height: 135px;
    background: var(--sky);
  }
  .company-line {
    position: absolute; right: 60px; top: 14px;
    color: var(--mist); font-weight: 900; font-size: 23px;
  }
  .experience-line {
    position: absolute; right: 60px; top: 46px;
    color: var(--navy); font-weight: 900; font-size: 21px;
  }
  .email {
    position: absolute; right: 60px; bottom: 14px;
    display: flex; align-items: center; gap: 12px;
    color: var(--paper); font-size: 19px;
  }
  .phone-strip {
    position: absolute; left: 0; right: 0; bottom: 0; height: 60px;
    background: var(--ink);
    display: flex; align-items: center; gap: 12px;
    padding-left: 60px;
    color: var(--mist); font-size: 19px; letter-spacing: .5px;
  }
</style>
</head>
<body>
  <section class="card card-back">
    <h2 class="headline">ARE YOU WORRIED<br>ABOUT YOUR TECHNOLOGY<br>RELIABILITY ?</h2>
    <p class="footer-strip">WE'LL ANSWER ALL YOUR TECHNOLOGY QUESTIONS</p>
  </section>

  <section class="card card-front">
    <div class="brand">
      <span class="brand-mark"></span>
      <span class="brand-name">VELVOR</span>
    </div>
    <p class="name-tag">MARCUS DREDGE</p>
    <p class="website">
      <svg width="14" height="14" viewBox="0 0 14 14" fill="none" stroke="#14285c" stroke-width="1.8"><path d="M6 8l2-2M5 5.5L3.5 7a2.1 2.1 0 003 3L8 8.5M9 8.5L10.5 7a2.1 2.1 0 00-3-3L6 5.5"/></svg>
      www.velvorit.com.au
    </p>
    <div class="info-band">
      <p class="company-line">VELVOR IT SERVICES</p>
      <p class="experience-line">12 YEARS EXPERIENCE IN THE IT INDUSTRY</p>
      <p class="email">
        <svg width="22" height="16" viewBox="0 0 22 16"><rect x="1" y="1" width="20" height="14" fill="#fff"/><path d="M1 1l10 8 10-8" fill="none" stroke="#33b5ea" stroke-width="1.6"/></svg>
        support@velvorit.com.au
      </p>
    </div>
    <p class="phone-strip">
      <svg width="20" height="18" viewBox="0 0 20 18" fill="#d9dde2"><path d="M2 5c0-2 3-3 8-3s8 1 8 3v2h-4V5H6v2H2z"/><rect x="4" y="8" width="12" height="9" rx="1.5"/></svg>
      0483 906 452
    </p>
  </section>
</body>
</html>
```